Interior designer needs a gorgeous, chic business card design.

A new, small Interior Design firm needs a business card that is chic, contemporary and elegant. Nothing over the top. My interiors are contemporary classic with an elegant feel to them. I like to use quality finishes and products rather than follow the latest fads. Projects can be anything from Pre start selections, bathrooms, kitchens, bedrooms, custom upholstery, furniture, rugs and art etc. The final design should display quality and an achievable sense of chic. I am open to all colours including black but not limited to this.

```html
<!DOCTYPE html>
<html lang="en">
<head>
<meta charset="utf-8">
<title>Vela Interiors – Business Card</title>
<link href="https://fonts.googleapis.com/css2?family=Lato:wght@300;400;700&display=swap" rel="stylesheet">
<style>
  :root {
    --backdrop: #e8e8e8;
    --card-light: #ffffff;
    --card-dark: #4a4747;
    --ink-soft: #8a8a8a;
    --ink-mid: #6e6e6e;
    --ink-strong: #2f2f2f;
    --logo-light: #f4f4f4;
  }
  * { margin: 0; padding: 0; box-sizing: border-box; }
  html, body {
    width: 1200px; height: 720px; overflow: hidden;
    background: var(--backdrop);
    font-family: "Lato", sans-serif;
  }
  .canvas { position: relative; width: 1200px; height: 720px; }

  .card {
    position: absolute; top: 210px;
    width: 520px; height: 300px;
    box-shadow: 0 2px 6px rgba(0,0,0,0.12);
  }

  /* Contact side */
  .card-contact { left: 50px; background: var(--card-light); color: var(--ink-soft); }
  .person { position: absolute; left: 36px; top: 34px; }
  .person-name {
    font-weight: 300; font-size: 27px; letter-spacing: 0.42em;
    line-height: 1.18; text-transform: uppercase; color: var(--ink-soft);
  }
  .qualification {
    margin-top: 6px; font-weight: 700; font-size: 9px;
    letter-spacing: 0.18em; color: var(--ink-mid);
  }
  .role {
    display: inline-block; margin-top: 12px;
    font-weight: 300; font-size: 15px; letter-spacing: 0.32em;
    border-bottom: 1px solid var(--ink-soft); padding-bottom: 2px;
  }
  .divider-stars { margin-top: 14px; margin-left: 30px; font-size: 14px; letter-spacing: 0.9em; }

  .details { position: absolute; right: 34px; top: 34px; text-align: left; width: 210px; }
  .address {
    font-weight: 300; font-size: 16px; letter-spacing: 0.38em;
    line-height: 1.35; color: var(--ink-mid); text-transform: uppercase;
  }
  .address .state { font-size: 9px; letter-spacing: 0.2em; text-decoration: underline; }
  .mobile-label {
    margin-top: 20px; font-size: 9px; font-weight: 400;
    letter-spacing: 0.45em; text-transform: uppercase;
  }
  .mobile-number {
    margin-top: 6px; font-weight: 400; font-size: 21px;
    letter-spacing: 0.3em; color: var(--ink-mid);
  }

  .contact-footer {
    position: absolute; left: 36px; right: 34px; bottom: 24px;
    display: flex; justify-content: space-between; align-items: baseline;
    font-size: 9px; letter-spacing: 0.3em; text-transform: uppercase;
  }
  .email { color: var(--ink-mid); }
  .email strong { color: var(--ink-strong); font-weight: 700; }
  .website strong { color: var(--ink-mid); font-weight: 700; }

  /* Brand side */
  .card-brand { left: 630px; background: var(--card-dark); overflow: hidden; }
  .brand-texture { position: absolute; inset: 0; background: var(--card-dark); }
  .brand-name {
    position: absolute; left: 0; right: 0; top: 92px; text-align: center;
    color: var(--logo-light); font-weight: 700; text-transform: uppercase;
  }
  .brand-name .main { display: block; font-size: 88px; line-height: 1; letter-spacing: 0.04em; }
  .brand-name .sub { display: block; margin-top: 6px; font-size: 15px; letter-spacing: 0.62em; padding-left: 0.62em; }
</style>
</head>
<body>
<main class="canvas">

  <section class="card card-contact" aria-label="Business card, contact side">
    <div class="person">
      <h1 class="person-name">Maren<br>Elise<br>Holloway</h1>
      <p class="qualification">(DIP. INTERIOR DESIGN)</p>
      <p class="role">DIRECTOR</p>
      <p class="divider-stars">* * *</p>
    </div>

    <div class="details">
      <p class="address">218<br>Harlow St<br>Melb. <span class="state">Vic</span> 3000</p>
      <p class="mobile-label">. . . Mobile . . .</p>
      <p class="mobile-number">0400555018</p>
    </div>

    <div class="contact-footer">
      <span class="email"><strong>maren</strong>@velainteriors.com.au</span>
      <span class="website">www.<strong>velainteriors</strong>.com</span>
    </div>
  </section>

  <section class="card card-brand" aria-label="Business card, brand side">
    <div class="brand-texture" role="img" aria-label="Subtle dark grey repeating pattern background"></div>
    <p class="brand-name">
      <span class="main">Vela</span>
      <span class="sub">Interiors</span>
    </p>
  </section>

</main>
</body>
</html>
```